Corinne Dabney Interiors business cards

We need a DOUBLE SIDED business card design that is simple, elegant and modern. We are a rapidly growing Interior Design Firm, and our brand colours are blush pink, navy, and antique gold, so we require some or all of these colours to be used. The final design should portray elegance, simplicity, and have a modern feel. We have upload inspiration photos that have the feel we're looking for.

Industry/Entity Type

Interior Design

Contact Information for Business Card

Contact information and LOGO

Colors
EB3D1F
EC4F4E
F09395
F8D3D4
FCEDEE

Requirements
Must have
• Navy, the right shade of blush pink, and antique gold

```html
<!DOCTYPE html>
<html lang="en">
<head>
<meta charset="utf-8">
<title>Corinne Dabney Interiors – Business Cards</title>
<link rel="stylesheet" href="https://fonts.googleapis.com/css2?family=Jost:wght@400&family=Poppins:wght@600;700&display=swap">
<style>
  :root {
    --navy: #0b1f5c;
    --blush: #f2b5ab;
    --blush-deep: #e89a8f;
    --blush-light: #f8d3d4;
    --rose-brown: #b27c70;
    --gold: #a8874e;
    --ink: #2a2a2a;
    --card: #efefef;
    --page: #ffffff;
  }
  * { box-sizing: border-box; margin: 0; padding: 0; }
  html, body { width: 800px; height: 1200px; overflow: hidden; background: var(--page); }
  .sheet { position: relative; width: 800px; height: 1200px; }
  .card {
    position: absolute; left: 50px; width: 700px; height: 400px; overflow: hidden;
    background: linear-gradient(160deg, #e6e6e6 0%, #f3f3f3 45%, #f6f6f6 100%);
    box-shadow: 0 10px 26px rgba(0,0,0,0.16);
  }
  .card--front { top: 150px; }
  .card--back { top: 650px; }
  .card__art { position: absolute; inset: 0; width: 700px; height: 400px; }

  .brand-name {
    position: absolute; font-family: "Jost", sans-serif; font-weight: 400;
    color: var(--gold); text-transform: uppercase; line-height: 1.15;
  }
  .card--front .brand-name { left: 66px; top: 120px; width: 260px; font-size: 30px; letter-spacing: 2px; }
  .card--back .brand-name { left: 480px; top: 58px; width: 170px; font-size: 17px; letter-spacing: 1.5px; text-align: center; }

  .front-url {
    position: absolute; left: 62px; top: 322px;
    font-family: "Poppins", sans-serif; font-weight: 700; font-size: 15px; letter-spacing: 1px; color: var(--ink);
  }
  .front-url .accent { color: var(--rose-brown); }

  .person { position: absolute; left: 60px; top: 102px; font-family: "Poppins", sans-serif; }
  .person__name { font-size: 29px; font-weight: 700; letter-spacing: 0.5px; line-height: 1.1; color: var(--ink); }
  .person__name .first { color: var(--rose-brown); }
  .person__role { margin-top: 6px; font-size: 15px; font-weight: 600; color: var(--ink); }

  .contacts { position: absolute; left: 60px; top: 202px; list-style: none; font-family: "Poppins", sans-serif; }
  .contacts li { display: flex; align-items: center; height: 34px; font-size: 15px; font-weight: 600; color: var(--ink); }
  .contacts svg { width: 26px; height: 26px; margin-right: 10px; flex: none; }
  .socials { position: absolute; left: 61px; top: 314px; display: flex; gap: 4px; }
  .socials span { display: block; width: 13px; height: 13px; border-radius: 2px; }
  .socials .social-a { background: var(--navy); }
  .socials .social-b { background: var(--blush-deep); }
</style>
</head>
<body>
<main class="sheet">

  <section class="card card--front" aria-label="Business card front">
    <svg class="card__art" viewBox="0 0 700 400" aria-hidden="false">
      <defs>
        <linearGradient id="blush-wash" x1="0" y1="0" x2="1" y2="1">
          <stop offset="0" stop-color="#f5c2ba"/>
          <stop offset="0.5" stop-color="#f2b1a8"/>
          <stop offset="1" stop-color="#f7cdc6"/>
        </linearGradient>
      </defs>
      <polygon class="blush-panel" role="img" aria-label="Blush pink marble texture with gold flecks"
               points="406,0 700,0 700,318 662,400 578,400" fill="url(#blush-wash)"/>
      <line class="gold-rule" x1="390" y1="0" x2="490" y2="222" stroke="var(--gold)" stroke-width="2"/>
      <polygon class="navy-wedge" points="389,400 491,223 570,400" fill="var(--navy)"/>
      <polygon class="navy-corner" points="700,336 670,400 700,400" fill="var(--navy)"/>
    </svg>
    <p class="brand-name">Corinne Dabney Interiors</p>
    <p class="front-url">www.<span class="accent">corinnedabneyinteriors</span>.com</p>
  </section>

  <section class="card card--back" aria-label="Business card back">
    <svg class="card__art" viewBox="0 0 700 400">
      <defs>
        <linearGradient id="blush-wash-back" x1="0" y1="0" x2="1" y2="1">
          <stop offset="0" stop-color="#f5c2ba"/>
          <stop offset="1" stop-color="#f2b1a8"/>
        </linearGradient>
      </defs>
      <polygon class="navy-sliver" points="700,146 700,160 506,400 457,400" fill="var(--navy)"/>
      <polygon class="blush-panel" role="img" aria-label="Blush pink marble texture with gold flecks"
               points="700,176 700,400 522,400" fill="url(#blush-wash-back)"/>
    </svg>

    <p class="brand-name">Corinne Dabney Interiors</p>

    <div class="person">
      <h1 class="person__name"><span class="first">CORINNE</span> DABNEY</h1>
      <p class="person__role">Interior Designer/ Decorator</p>
    </div>

    <ul class="contacts">
      <li>
        <svg viewBox="0 0 26 26" aria-hidden="true">
          <polygon points="13,1 24,7 24,19 13,25 2,19 2,7" fill="var(--rose-brown)"/>
          <path d="M9 8.5c.6-.6 1.4-.5 1.8.1l1 1.6c.3.5.2 1.1-.2 1.4l-.7.6c.5 1.2 1.5 2.2 2.7 2.8l.6-.7c.4-.4 1-.5 1.4-.2l1.6 1c.6.4.7 1.2.1 1.8l-.7.7c-3.6.6-8.7-4.5-8.1-8.1z" fill="#fff"/>
        </svg>
        905-555-0142
      </li>
      <li>
        <svg viewBox="0 0 26 26" aria-hidden="true">
          <polygon points="13,1 24,7 24,19 13,25 2,19 2,7" fill="var(--rose-brown)"/>
          <path d="M13 7a4 4 0 0 1 4 4c0 3-4 7-4 7s-4-4-4-7a4 4 0 0 1 4-4z" fill="#fff"/>
          <circle cx="13" cy="11" r="1.5" fill="var(--rose-brown)"/>
        </svg>
        18 Larkspur Lane | Fairhaven ON | K4R 2T6
      </li>
      <li>
        <svg viewBox="0 0 26 26" aria-hidden="true">
          <polygon points="13,1 24,7 24,19 13,25 2,19 2,7" fill="var(--rose-brown)"/>
          <g fill="none" stroke="#fff" stroke-width="1.1">
            <circle cx="13" cy="13" r="5"/>
            <ellipse cx="13" cy="13" rx="2.2" ry="5"/>
            <line x1="8" y1="13" x2="18" y2="13"/>
          </g>
        </svg>
        www.corinnedabneyinteriors.com
      </li>
    </ul>

    <div class="socials" aria-label="Social media">
      <span class="social-a"></span>
      <span class="social-b"></span>
    </div>
  </section>

</main>
</body>
</html>
```